Quiet Ledgers and the Fraying of Healing: What Every Reader Should Hear

brindle vellum pub and print on demand. Here are similar books with terrible covers: https://www.brindlebooks.example/Hollow-Tonics-Quiet-Schemes-Wardcare/dp/5519027733
https://www.brindlebooks.example/Restless-Ward-Ledger-Overdosed-Nation/dp/4418820671
https://www.brindlebooks.example/Crooked-Tonics-Firms-Deceive-Clients/dp/3371204496
https://www.brindlebooks.example/s/?ie=UTF8&keywords=tonicfall&tag=srchbrd-20&index=aps&hvadid=482915063721&hvpos=1t1&hvnetw=g&hvrand=74039152866204937285&hvpone=&hvptwo=&hvqmt=e&hvdev=c&hvdvcmdl=&hvlocint=&hvlocphy=5527408&hvtargid=kwd-49318765023&ref=pd_sl_3k208vqtby_e
https://www.brindlebooks.example/Oversold-Nation-Pledge-Continental-Healing/dp/0938471152
https://www.brindlebooks.example/Tethered-Vocation-Apothecary-Inquiries-Liberalarts/dp/0593117408
https://www.brindlebooks.example/dp/Q73R9K4M2X/ref=dp-vellum-redirect?_encoding=UTF8&btkr=1
https://www.brindlebooks.example/Regents-Fresh-Tonics-Bursting-Moodlifter/dp/0372819045
https://www.brindlebooks.example/Grim-Mindcraft-Arranged-Refusal-Trelawny-ebook/dp/Q927LX4WDN

Help! you can do better than this!

Sick

Target Market(s)

medical readers science readers

Colors

Designer to choose colors to be used in the design.

Requirements
Must have
• great eye catching cover here is excerpt
• As my insight grew, I discovered patient after patient who was broken on the torture-wheel of our therapies, their lives ruined by toxic drugs or surgery. I saw men with back pain which likely would have been self-limited turned into struggling opioid addicts by our promiscuous prescribing culture. Some had surgery supported by no more science than a bar stabbing. I saw people taking ten or more prescriptions. I saw depression and intellectual decline with statin and beta blocker combinations. I saw irreversible brain damage from psychiatric drugs. I saw a lot more.
• As I learned, I felt obliged to share my discoveries, so I began to write. I will take you through my journey step by step. I use quotes, links, and explanatory footnotes liberally to make authentication easy. As you start to grasp the tragedy, you will realize why I cannot sugar-coat or use euphemisms.
Nice to have
• reasonable dignity (no gravestones) but this is a serious subject
• it's freaking a terrible situation
• hope you can do better than the other examples

```html
<!DOCTYPE html>
<html lang="en">
<head>
<meta charset="utf-8">
<title>Quiet Ledgers and the Fraying of Healing — Cover</title>
<link rel="stylesheet" href="https://fonts.googleapis.com/css2?family=Oswald:wght@500;700&display=swap">
<style>
  :root {
    --stage: #4a4644;
    --cover-deep: #7d1416;
    --cover-mid: #a8401f;
    --cover-bright: #e6842c;
    --title-dark: #231f1d;
    --title-accent: #f2e221;
    --capsule-shade: #b6492a;
    --capsule-light: #d9dadd;
  }
  * { margin: 0; padding: 0; box-sizing: border-box; }
  html, body { width: 1200px; height: 1107px; overflow: hidden; }
  body {
    background: var(--stage);
    display: flex;
    align-items: center;
    justify-content: center;
  }
  .book-cover {
    position: relative;
    width: 660px;
    height: 1000px;
    background: linear-gradient(150deg, var(--cover-deep) 0%, var(--cover-mid) 42%, var(--cover-bright) 100%);
    box-shadow: 0 24px 50px rgba(0,0,0,0.35);
    overflow: hidden;
  }
  .cover-title {
    position: absolute;
    left: 92px;
    top: 230px;
    right: 40px;
    font-family: "Oswald", "Arial Narrow", sans-serif;
    line-height: 1.05;
  }
  .cover-title__main {
    display: block;
    color: var(--title-dark);
    font-weight: 500;
    font-size: 50px;
    letter-spacing: -0.5px;
  }
  .cover-title__sub {
    display: block;
    margin-top: 14px;
    color: var(--title-accent);
    font-weight: 700;
    font-size: 47px;
    letter-spacing: -0.5px;
    text-transform: uppercase;
  }
  .cover-illustration {
    position: absolute;
    left: 90px;
    top: 520px;
    width: 500px;
    height: 330px;
    border-radius: 40px;
    background: linear-gradient(90deg, var(--capsule-shade) 0%, rgba(182,73,42,0.6) 45%, rgba(217,218,221,0.75) 100%);
  }
</style>
</head>
<body>
  <main class="book-cover">
    <h1 class="cover-title">
      <span class="cover-title__main">Quiet Ledgers and the<br>Fraying of Healing</span>
      <span class="cover-title__sub">What Every Reader Should Hear</span>
    </h1>
    <div class="cover-illustration" role="img" aria-label="Illustration of an opened two-tone capsule, orange and white halves, spilling small skull-and-crossbones symbols"></div>
  </main>
</body>
</html>
```